Tallow Crest Software PowerPoint template

We are a software company selling endpoint visibility, access and security technology to enterprise-level IT departments.
Our technology helps organizations gain comprehensive visibility into and control over devices accessing their corporate network so they can quickly identify and address suspicious activity on the network that could lead to potential threats like data breaches.
This technology can cost organizations upwards of $1M - depending on the size of the organization. Our primary clients are Meridane 2,000 companies.
We want a professional, polished PowerPoint template that we can use for all company presentations. Please include:
Title page
Section page
General info page
Thank you page
Logo options and color specs are attached.
Please include our tagline on at least the title page: Discover the edge. Optimize the whole.

```html
<!DOCTYPE html>
<html lang="en">
<head>
<meta charset="UTF-8">
<title>Tallow Crest Software – Section Slide</title>
<link href="https://fonts.googleapis.com/css2?family=Montserrat:wght@600&family=Roboto:wght@400&display=swap" rel="stylesheet">
<style>
  :root {
    --slide-red: #8c0007;
    --slide-red-soft: #960a10;
    --accent-orange: #e07a4b;
    --footer-orange: #de7d55;
    --ring-red: #c0281f;
    --icon-line: #d98c8a;
    --footer-text: #ffffff;
  }
  html, body {
    margin: 0;
    padding: 0;
    width: 1200px;
    height: 900px;
    overflow: hidden;
    background: var(--slide-red);
  }
  .slide {
    position: relative;
    width: 1200px;
    height: 900px;
    overflow: hidden;
  }
  .slide-backdrop {
    position: absolute;
    inset: 0;
    background: radial-gradient(circle at 50% 45%, var(--slide-red-soft) 0%, var(--slide-red) 75%);
  }
  .section-icon {
    position: absolute;
    left: 500px;
    top: 305px;
    width: 140px;
    height: 140px;
  }
  .section-title {
    position: absolute;
    left: 0;
    right: 0;
    top: 468px;
    margin: 0;
    text-align: center;
    font-family: "Montserrat", sans-serif;
    font-weight: 600;
    font-size: 64px;
    letter-spacing: 0.5px;
    color: var(--accent-orange);
    line-height: 1;
  }
  .slide-footer {
    position: absolute;
    left: 0;
    right: 0;
    bottom: 0;
    height: 42px;
    background: var(--footer-orange);
    display: flex;
    align-items: center;
    justify-content: space-between;
    padding: 0 12px;
    font-family: "Roboto", sans-serif;
    font-size: 17px;
    color: var(--footer-text);
  }
</style>
</head>
<body>
  <main class="slide">
    <div class="slide-backdrop" role="img" aria-label="Deep red background with a soft polka dot pattern"></div>

    <svg class="section-icon" viewBox="0 0 140 140" aria-hidden="true">
      <circle cx="70" cy="70" r="67" fill="none" stroke="var(--ring-red)" stroke-width="4"/>
      <g fill="none" stroke="var(--icon-line)" stroke-width="2.5" stroke-linecap="round" stroke-linejoin="round">
        <path d="M60 88 C60 78 44 70 44 52 A26 26 0 0 1 96 52 C96 70 80 78 80 88 Z"/>
        <path d="M64 88 L64 66 C64 58 70 58 70 64 C70 58 76 58 76 66 L76 88"/>
        <line x1="60" y1="94" x2="80" y2="94"/>
        <line x1="60" y1="100" x2="80" y2="100"/>
        <line x1="62" y1="106" x2="78" y2="106"/>
        <line x1="66" y1="112" x2="74" y2="112"/>
      </g>
    </svg>

    <h1 class="section-title">SLIDE SECTION SLIDE</h1>

    <footer class="slide-footer">
      <span class="footer-copyright">COPYRIGHT TEXT HERE</span>
      <span class="footer-page">Page : 01</span>
    </footer>
  </main>
</body>
</html>
```